Apartment services app

The app should permit current residents to pay rent, submit work orders or submit comments and general requests. There is an app that is available from Heron Works in the UK that could be used to benchmark, but I would like to see something more appropriate for the US.
Updates

The company name for this project is Oakfield Property Management. We will be providing a logo at a later date as we we will be submitting a separate design project for the development of a new logo.

Reason: I am extending the deadline by another week so that I may comment on the designs so far and each of you will have time to respond Tim

Target Market(s)

Residents of our apartment communities

Industry/Entity Type

Apartment

Requirements
Must have
• Ability to pay rent
• Ability to have reminders sent to resident
• Notices sent to resident
• Resident able to submit work order requests
• Resident able to submit comments and complaints

```html
<!DOCTYPE html>
<html lang="en">
<head>
<meta charset="utf-8">
<title>Oakfield Property Management — Resident App</title>
<link rel="stylesheet" href="https://fonts.googleapis.com/css2?family=Bebas+Neue&family=Open+Sans:wght@300;400;600;700&display=swap">
<style>
  :root {
    --status-bg: #2f3034;
    --header-bg: #6d7078;
    --grid-bg: #f4f4f4;
    --panel-bg: #ffffff;
    --circle-dark: #45464b;
    --accent: #29b8d4;
    --label: #38393d;
    --label-muted: #6a6b70;
    --tabbar-bg: #4b4c51;
    --tabbar-line: #5d5e63;
    --tabbar-text: #e6e6e8;
    --badge: #e8585b;
    --white: #ffffff;
    --rule: #d6d6d8;
  }
  * { box-sizing: border-box; margin: 0; padding: 0; }
  html, body { width: 757px; height: 1200px; overflow: hidden; background: var(--grid-bg); }
  .app { position: relative; width: 757px; height: 1200px; font-family: "Open Sans", sans-serif; overflow: hidden; }

  .status-bar { position: absolute; left: 0; top: 0; width: 100%; height: 40px; background: var(--status-bg);
    color: var(--white); font-family: "Open Sans", sans-serif; font-weight: 700; font-size: 24px; }
  .status-bar .carrier { position: absolute; left: 12px; top: 4px; display: flex; align-items: center; gap: 6px; }
  .status-bar .time { position: absolute; left: 0; right: 0; top: 4px; text-align: center; }
  .status-bar .battery { position: absolute; right: 12px; top: 4px; display: flex; align-items: center; gap: 8px; }

  .app-header { position: absolute; left: 0; top: 40px; width: 100%; height: 108px; background: var(--header-bg);
    display: flex; align-items: center; justify-content: center; }
  .app-header .title { color: var(--white); font-weight: 400; font-size: 25px; letter-spacing: 0.2px; }
  .app-header .header-icon { position: absolute; top: 37px; }
  .app-header .settings { left: 44px; }
  .app-header .help { right: 40px; }

  .resident-grid { position: absolute; left: 0; top: 148px; width: 100%; height: 638px; background: var(--grid-bg); }
  .tile { position: absolute; width: 220px; margin-left: -110px; text-align: center; }
  .tile .circle { position: relative; width: 140px; height: 140px; border-radius: 50%; margin: 0 auto;
    background: var(--circle-dark); display: flex; align-items: center; justify-content: center; }
  .tile .label { margin-top: 18px; font-family: "Bebas Neue", sans-serif; font-size: 25px; color: var(--label); letter-spacing: 0.3px; }
  .tile .label.muted { color: var(--label-muted); }
  .badge { position: absolute; top: 0; right: 2px; width: 30px; height: 30px; border-radius: 50%; background: var(--badge);
    color: var(--white); font-size: 15px; font-weight: 600; display: flex; align-items: center; justify-content: center; }

  .section-tab { position: absolute; left: 170px; top: 747px; width: 404px; height: 40px; background: var(--panel-bg);
    border: 1px solid var(--rule); border-bottom: none; text-align: center; line-height: 38px;
    font-size: 19px; color: #55565b; letter-spacing: 0.3px; z-index: 2; }
  .management-panel { position: absolute; left: 0; top: 786px; width: 100%; height: 297px; background: var(--panel-bg);
    border-top: 1px solid var(--rule); }
  .management-panel .circle { background: var(--accent); }

  .tab-bar { position: absolute; left: 0; top: 1083px; width: 100%; height: 117px; background: var(--tabbar-bg); display: flex; }
  .tab { flex: 1; display: flex; flex-direction: column; align-items: center; justify-content: center; gap: 12px;
    color: var(--tabbar-text); font-size: 17px; border-right: 1px solid var(--tabbar-line); }
  .tab:last-child { border-right: none; }
</style>
</head>
<body>
<div class="app">
  <div class="status-bar">
    <div class="carrier">
      <svg width="34" height="20" viewBox="0 0 34 20" fill="#fff"><rect x="0" y="13" width="5" height="7"/><rect x="7" y="10" width="5" height="10"/><rect x="14" y="7" width="5" height="13"/><rect x="21" y="4" width="5" height="16"/><rect x="28" y="1" width="5" height="19"/></svg>
      <span>ORBIT</span>
    </div>
    <div class="time">10:35 AM</div>
    <div class="battery">
      <svg width="20" height="20" viewBox="0 0 20 20"><circle cx="10" cy="10" r="9" fill="#fff"/><path d="M10 4v6h4" stroke="#2f3034" stroke-width="2" fill="none"/></svg>
      <span>65%</span>
      <svg width="46" height="24" viewBox="0 0 46 24"><rect x="1" y="2" width="40" height="20" rx="3" fill="none" stroke="#fff" stroke-width="2"/><rect x="4" y="5" width="24" height="14" fill="#fff"/><rect x="42" y="8" width="3" height="8" fill="#fff"/></svg>
    </div>
  </div>

  <header class="app-header">
    <svg class="header-icon settings" width="34" height="34" viewBox="0 0 24 24" fill="none" stroke="#fff" stroke-width="1.2"><circle cx="12" cy="12" r="3.2"/><path d="M12 2.5l1.6 2.3 2.7-.8.6 2.8 2.7.9-.9 2.7 2.3 1.6-2.3 1.6.9 2.7-2.7.9-.6 2.8-2.7-.8L12 21.5l-1.6-2.3-2.7.8-.6-2.8-2.7-.9.9-2.7L2.5 12l2.3-1.6-.9-2.7 2.7-.9.6-2.8 2.7.8z"/></svg>
    <h1 class="title">Oakfield Property Management</h1>
    <svg class="header-icon help" width="34" height="34" viewBox="0 0 34 34" fill="none" stroke="#fff" stroke-width="1.5"><circle cx="17" cy="17" r="15"/><text x="17" y="23" text-anchor="middle" font-family="Open Sans, sans-serif" font-size="17" fill="#fff" stroke="none">?</text></svg>
  </header>

  <main class="resident-grid">
    <div class="tile" style="left:150px; top:98px;">
      <div class="circle">
        <svg width="76" height="64" viewBox="0 0 76 64" fill="#fff"><g transform="translate(24 38)"><circle r="15"/><g><rect x="-5" y="-21" width="10" height="42"/><rect x="-5" y="-21" width="10" height="42" transform="rotate(45)"/><rect x="-5" y="-21" width="10" height="42" transform="rotate(90)"/><rect x="-5" y="-21" width="10" height="42" transform="rotate(135)"/></g><circle r="6" fill="#45464b"/></g><g transform="translate(54 18)"><circle r="10"/><rect x="-3.5" y="-14" width="7" height="28"/><rect x="-3.5" y="-14" width="7" height="28" transform="rotate(45)"/><rect x="-3.5" y="-14" width="7" height="28" transform="rotate(90)"/><rect x="-3.5" y="-14" width="7" height="28" transform="rotate(135)"/><circle r="4" fill="#45464b"/></g></svg>
      </div>
      <div class="label">Request Services</div>
    </div>
    <div class="tile" style="left:379px; top:98px;">
      <div class="circle">
        <svg width="74" height="60" viewBox="0 0 74 60" fill="#fff" stroke="#45464b" stroke-width="2"><ellipse cx="52" cy="12" rx="18" ry="7"/><rect x="34" y="12" width="36" height="30"/><ellipse cx="52" cy="42" rx="18" ry="7"/><path d="M34 22q18 9 36 0M34 32q18 9 36 0" fill="none"/><ellipse cx="22" cy="28" rx="18" ry="7"/><rect x="4" y="28" width="36" height="22"/><ellipse cx="22" cy="50" rx="18" ry="7"/><path d="M4 39q18 9 36 0" fill="none"/></svg>
      </div>
      <div class="label">Pay Rent</div>
    </div>
    <div class="tile" style="left:618px; top:98px;">
      <div class="circle">
        <svg width="50" height="60" viewBox="0 0 50 60" fill="none" stroke="#fff" stroke-width="3"><rect x="3" y="3" width="44" height="54" rx="2"/><g fill="#fff" stroke="none"><rect x="11" y="15" width="4" height="4"/><rect x="11" y="25" width="4" height="4"/><rect x="11" y="35" width="4" height="4"/><rect x="11" y="45" width="4" height="4"/><rect x="19" y="16" width="20" height="2"/><rect x="19" y="26" width="20" height="2"/><rect x="19" y="36" width="20" height="2"/><rect x="19" y="46" width="20" height="2"/></g></svg>
      </div>
      <div class="label muted">Work Orders</div>
    </div>

    <div class="tile" style="left:150px; top:323px;">
      <div class="circle">
        <svg width="60" height="66" viewBox="0 0 60 66" fill="#fff"><path d="M10 6c-6 0-8 4-8 8v42c0 4 4 6 8 6s6-2 6-6V14c0-4-2-8-6-8z" fill="none" stroke="#fff" stroke-width="3"/><rect x="20" y="4" width="38" height="56" rx="4"/><rect x="26" y="10" width="26" height="12" fill="#45464b"/><g fill="#45464b"><rect x="26" y="28" width="6" height="5"/><rect x="36" y="28" width="6" height="5"/><rect x="46" y="28" width="6" height="5"/><rect x="26" y="37" width="6" height="5"/><rect x="36" y="37" width="6" height="5"/><rect x="46" y="37" width="6" height="5"/><rect x="26" y="46" width="6" height="5"/><rect x="36" y="46" width="6" height="5"/><rect x="46" y="46" width="6" height="5"/></g></svg>
      </div>
      <div class="label">Contact</div>
    </div>
    <div class="tile" style="left:379px; top:323px;">
      <div class="circle" role="img" aria-label="Security officer icon"></div>
      <div class="label">Report</div>
    </div>
    <div class="tile" style="left:618px; top:323px;">
      <div class="circle">
        <svg width="56" height="62" viewBox="0 0 56 62" fill="#fff"><ellipse cx="28" cy="18" rx="14" ry="16"/><path d="M2 62c0-16 10-24 26-24s26 8 26 24z"/></svg>
        <span class="badge">3</span>
      </div>
      <div class="label">My Request</div>
    </div>
  </main>

  <div class="section-tab">MANAGEMENT SERVICES</div>
  <section class="management-panel">
    <div class="tile" style="left:150px; top:46px;">
      <div class="circle">
        <svg width="70" height="64" viewBox="0 0 70 64" fill="#fff"><g transform="rotate(-25 35 32)"><path d="M35 6c-12 0-18 10-18 22v12l-6 8h48l-6-8V28c0-12-6-22-18-22z"/><circle cx="35" cy="4" r="4"/><circle cx="35" cy="54" r="6"/></g><path d="M6 40q-4 14 14 20" fill="none" stroke="#fff" stroke-width="3"/></svg>
      </div>
      <div class="label">Announcements</div>
    </div>
    <div class="tile" style="left:379px; top:46px;">
      <div class="circle">
        <svg width="82" height="50" viewBox="0 0 82 50" fill="#fff"><circle cx="41" cy="12" r="10"/><circle cx="20" cy="17" r="8"/><circle cx="62" cy="17" r="8"/><path d="M26 40c0-10 7-16 15-16s15 6 15 16z"/><path d="M6 42c0-8 6-13 14-13 4 0 6 1 8 3-3 3-4 6-4 10z"/><path d="M76 42c0-8-6-13-14-13-4 0-6 1-8 3 3 3 4 6 4 10z"/><path d="M2 40q39 18 78 0v4q-39 16-78 0z"/></svg>
      </div>
      <div class="label">Send Messages</div>
    </div>
    <div class="tile" style="left:618px; top:46px;">
      <div class="circle">
        <svg width="60" height="56" viewBox="0 0 60 56" fill="#fff"><rect x="4" y="4" width="52" height="48"/><path d="M12 30L30 14l18 16v18H12z" fill="#29b8d4"/><rect x="26" y="34" width="8" height="14" fill="#fff"/><path d="M8 10h44" stroke="#29b8d4" stroke-width="2"/></svg>
      </div>
      <div class="label">Contracts</div>
    </div>
  </section>

  <nav class="tab-bar">
    <div class="tab">
      <svg width="40" height="40" viewBox="0 0 40 40" fill="none" stroke="#e6e6e8" stroke-width="1.6"><ellipse cx="20" cy="13" rx="8" ry="10"/><path d="M4 38c0-10 6-14 16-14s16 4 16 14z"/></svg>
      <span>My Account</span>
    </div>
    <div class="tab">
      <svg width="40" height="40" viewBox="0 0 40 40" fill="none" stroke="#e6e6e8" stroke-width="1.6"><path d="M36 8l-6 6-4-4 6-6c-5-2-11 1-11 7 0 2 0 3 1 4L4 31c-2 2-2 4 0 5s3 2 5 0l16-17c1 1 2 1 4 1 6 0 9-6 7-12z"/></svg>
      <span>Services</span>
    </div>
    <div class="tab">
      <svg width="40" height="40" viewBox="0 0 40 40" fill="none" stroke="#e6e6e8" stroke-width="1.6"><ellipse cx="26" cy="7" rx="11" ry="4"/><path d="M15 7v18q11 6 22 0V7M15 13q11 6 22 0M15 19q11 6 22 0"/><ellipse cx="14" cy="20" rx="11" ry="4"/><path d="M3 20v14q11 6 22 0V20M3 27q11 6 22 0"/></svg>
      <span>Rents</span>
    </div>
    <div class="tab">
      <svg width="40" height="40" viewBox="0 0 24 24" fill="none" stroke="#e6e6e8" stroke-width="1"><circle cx="12" cy="12" r="3.2"/><path d="M12 2.5l1.6 2.3 2.7-.8.6 2.8 2.7.9-.9 2.7 2.3 1.6-2.3 1.6.9 2.7-2.7.9-.6 2.8-2.7-.8L12 21.5l-1.6-2.3-2.7.8-.6-2.8-2.7-.9.9-2.7L2.5 12l2.3-1.6-.9-2.7 2.7-.9.6-2.8 2.7.8z"/></svg>
      <span>Settings</span>
    </div>
  </nav>
</div>
</body>
</html>
```